I had to make an update to properly guide your designs.
I need a brochure for a company called Ferrand Calloway Ltd. all details you need can be found in the attached files including content in a microsoft word file. in the word file you will see the content you need please use them. you can. It is a consulting, construction and real estate company. You are free to add other relevant picture of yours that can make more sense. i have also attached the pictures needed. the word file show the usage of the pictures and the required content for them. It is pertinent to keep the design professional.
please be creative without the design appearing too crowded.
Updates
I had to make an update to properly guide your designs. i have attached a microsoft word file and pictures

```html
<!DOCTYPE html>
<html lang="en">
<head>
<meta charset="utf-8">
<title>Ferrand Calloway Ltd. – Company Brochure</title>
<link href="https://fonts.googleapis.com/css2?family=Cinzel:wght@400;600&family=Open+Sans:wght@400;600&family=Arimo:wght@400;700&display=swap" rel="stylesheet">
<style>
:root{
  --stage:#8c8c8c;
  --navy:#0d2a4a;
  --deep-blue:#123a63;
  --teal:#2f7f8c;
  --sky:#22a4dc;
  --red:#d92b35;
  --red-dark:#a8161f;
  --charcoal:#222428;
  --ink:#2b2b2b;
  --paper:#ffffff;
  --soft-white:rgba(255,255,255,.85);
}
*{box-sizing:border-box;margin:0;padding:0}
html,body{width:1200px;height:1080px;overflow:hidden}
body{background:radial-gradient(ellipse at 50% 35%,#b3b3b3,var(--stage) 75%);font-family:"Arimo",Arial,sans-serif;position:relative}

.sheet{position:absolute;box-shadow:0 10px 28px rgba(0,0,0,.35);overflow:hidden}

/* front cover */
.front-cover{left:70px;top:40px;width:340px;height:480px;background:linear-gradient(170deg,var(--deep-blue),var(--navy) 55%,#2a2d33)}
.front-cover .cover-photo{position:absolute;left:0;top:0;width:100%;height:330px;background:linear-gradient(160deg,#1f5f7a,var(--teal) 45%,#1b3f56);clip-path:polygon(0 0,100% 0,100% 88%,0 100%)}
.front-cover .tagline{position:absolute;left:26px;top:300px;color:#cfe7f5}
.tagline .tag-main{font-family:"Cinzel",serif;font-size:24px;letter-spacing:1px;line-height:1}
.tagline .tag-sub{font-family:"Open Sans",sans-serif;font-size:17px;color:#fff;margin-top:4px}
.front-cover .cover-brand{position:absolute;left:26px;bottom:28px}
.brand-name{font-family:"Open Sans",sans-serif;font-weight:600;font-size:13px;color:var(--red);letter-spacing:.5px;display:flex;align-items:center;gap:6px}
.brand-name .brand-dot{width:8px;height:8px;border-radius:50%;background:var(--red)}
.brand-web{font-family:"Open Sans",sans-serif;font-size:8px;color:#d6d6d6;letter-spacing:2px;margin-top:4px}

/* back cover */
.back-cover{left:790px;top:40px;width:340px;height:480px;background:var(--red)}
.back-cover .back-photo{position:absolute;left:0;top:0;width:290px;height:400px;background:linear-gradient(150deg,#b71c26,var(--red) 50%,#c4222c)}
.back-cover .blue-band{position:absolute;right:0;top:0;width:50px;height:400px;background:var(--sky)}
.back-cover .contact{position:absolute;right:70px;top:230px;text-align:right;color:#fff;font-size:9px;line-height:1.75}
.back-cover .back-foot{position:absolute;left:0;bottom:0;width:100%;height:80px;background:var(--charcoal);display:flex;flex-direction:column;align-items:center;justify-content:center}

/* inner spread */
.spread{left:160px;top:570px;width:880px;height:480px;display:flex}
.page{position:relative;width:440px;height:100%;overflow:hidden}
.page-company{background:linear-gradient(90deg,var(--paper) 85%,#e6e6e6)}
.site-photo{position:absolute;left:22px;top:20px;width:240px;height:120px;border-radius:0 40px 0 0;background:linear-gradient(160deg,#8fa3b3,#a38e72 60%,#6c6a62)}
.page-company .rule{position:absolute;left:22px;top:158px;width:380px;height:1px;background:var(--sky)}
.section-title{font-family:"Cinzel",serif;font-size:15px;color:var(--red);letter-spacing:.5px}
.company-copy{position:absolute;left:22px;top:164px;width:380px}
.company-copy p{font-size:7.2px;line-height:1.45;color:var(--ink);margin-top:6px}
.company-copy .sub-title{font-family:"Arimo",sans-serif;font-weight:700;font-size:11px;color:var(--red);margin-top:9px}
.team-photo{position:absolute;left:22px;bottom:18px;width:230px;height:108px;border-radius:0 30px 0 0;background:linear-gradient(170deg,#b9c2c8,#6f7a80 70%,#3c4246)}

.page-services{background:linear-gradient(180deg,var(--red),var(--red-dark))}
.services{position:absolute;left:18px;top:12px;width:260px;color:#fff}
.services .section-title{color:#fff;border-bottom:1px solid var(--soft-white);padding-bottom:3px}
.service-head{font-weight:700;font-size:10px;margin-top:6px}
.services ul{list-style:none;margin-top:1px}
.services li{font-size:6.6px;line-height:1.45;padding-left:7px;position:relative}
.services li::before{content:"";position:absolute;left:0;top:3px;width:3px;height:3px;background:#fff}
.service-photo{width:240px;height:62px;border-radius:14px 0 14px 0;margin-top:5px}
.photo-site{background:linear-gradient(170deg,#9bb2a0,#8c7a5e)}
.photo-paving{background:linear-gradient(170deg,#b7c3cf,#8e9296)}
.photo-building{background:linear-gradient(170deg,#cfdce8,#a7a49e)}

.specialties{position:absolute;right:10px;top:14px;width:140px;height:450px;border-left:1px solid var(--soft-white)}
.specialty{position:relative;height:90px;border-bottom:1px solid var(--soft-white);display:flex;flex-direction:column;align-items:center;justify-content:center}
.specialty-photo{width:58px;height:58px;border-radius:50%;border:2px solid #fff;background:radial-gradient(circle at 40% 35%,#a9b0a8,#5b5f58)}
.specialty-label{font-size:7px;font-weight:700;color:#fff;margin-top:4px}
</style>
</head>
<body>

<section class="sheet front-cover" aria-label="Front cover">
  <div class="cover-photo" role="img" aria-label="Photograph of a modern curved apartment tower in blue tones"></div>
  <div class="tagline">
    <div class="tag-main">WE BUILD YOUR DREAMS</div>
    <div class="tag-sub">one at a time</div>
  </div>
  <div class="cover-brand">
    <div class="brand-name"><span class="brand-dot"></span>Ferrand Calloway Ltd.</div>
    <div class="brand-web">ferrandcalloway.com</div>
  </div>
</section>

<section class="sheet back-cover" aria-label="Back cover">
  <div class="back-photo" role="img" aria-label="Red-tinted architectural elevation of a building facade"></div>
  <div class="blue-band"></div>
  <address class="contact" style="font-style:normal">
    14, Marlowe street, off Harbour link Road,<br>
    Ikeja Lagos, Nigeria<br>
    +234 10000 4821<br>
    +234 7000 5519 36<br>
    info@ferrandcalloway.com
  </address>
  <div class="back-foot">
    <div class="brand-name"><span class="brand-dot"></span>Ferrand Calloway Ltd.</div>
    <div class="brand-web">ferrandcalloway.com</div>
  </div>
</section>

<section class="sheet spread" aria-label="Inner spread">
  <article class="page page-company">
    <div class="site-photo" role="img" aria-label="Photograph of workers on a construction site laying concrete"></div>
    <div class="rule"></div>
    <div class="company-copy">
      <h2 class="section-title">THE COMPANY</h2>
      <p>Ferrand Calloway Ltd. is a value based infrastructure development and real estate company. We are involved in planning, designing, construction and management of infrastructure development. We believe in the long-term values that shape all civil works: transportation, energy and the need for people to live and work well. We are proud of our ability to create and deliver good solutions to our clients, whether in construction, engineering consulting or real estate.</p>
      <p>Our company is founded on a strong belief in our core values. We have a real commitment to innovation and the support of good ideas. The firm is built upon years of experience in the Nigerian construction, consulting and real estate environment.</p>
      <h3 class="sub-title">OUR AIM</h3>
      <p>Our mission is to develop a global infrastructure development company that will represent true industry standards and be a conspicuous player not only in Nigeria but Africa and the world over.</p>
      <p>Excellence in service remains the major driving force of the firm in the built environment. We have core values that provide guiding principles for everyone at Ferrand Calloway; these values help us work together and with others to provide a better place to work, a better service to our clients, and support to the communities in which we work.</p>
    </div>
    <div class="team-photo" role="img" aria-label="Photograph of the project team reviewing a site plan outdoors"></div>
  </article>

  <article class="page page-services">
    <div class="services">
      <h2 class="section-title">OUR SERVICES</h2>
      <div class="service-head">CONSULTING</div>
      <ul>
        <li>Road design</li>
        <li>Building structural design</li>
        <li>Storm and waste water sewer systems</li>
        <li>Large drainage network design</li>
        <li>Infrastructure planning for large area developments</li>
        <li>Flood assessment, mitigation and hydraulic modelling</li>
        <li>Land survey, contour mapping, terrain modelling</li>
        <li>Wastewater treatment system</li>
        <li>Mechanical and electrical infrastructure design</li>
        <li>Project management</li>
        <li>Aerial photography and video</li>
      </ul>
      <div class="service-photo photo-site" role="img" aria-label="Aerial photograph of a drainage channel under construction"></div>
      <div class="service-head">CONSTRUCTION</div>
      <ul>
        <li>Road construction</li>
        <li>Commercial and residential building construction</li>
        <li>Storm water drainage construction</li>
        <li>Sewer networks and treatment plant construction</li>
        <li>Civil works construction</li>
        <li>Electrification</li>
      </ul>
      <div class="service-photo photo-paving" role="img" aria-label="Photograph of a newly paved interlocking road surface"></div>
      <div class="service-head">REAL ESTATE</div>
      <ul>
        <li>Commercial property development and leasing</li>
        <li>Residential property development and leasing</li>
      </ul>
      <div class="service-photo photo-building" role="img" aria-label="Rendering of a modern multi-storey office building"></div>
    </div>

    <div class="specialties">
      <div class="specialty"><div class="specialty-photo" role="img" aria-label="Photograph of a large culvert pipe"></div><div class="specialty-label">Flood Risk Management</div></div>
      <div class="specialty"><div class="specialty-photo" role="img" aria-label="Photograph of an excavated canal"></div><div class="specialty-label">Canal and Waterway</div></div>
      <div class="specialty"><div class="specialty-photo" role="img" aria-label="Aerial photograph of a highway interchange"></div><div class="specialty-label">Geospatial Solutions</div></div>
      <div class="specialty"><div class="specialty-photo" role="img" aria-label="Photograph of a road construction machine"></div><div class="specialty-label">Highway Engineering</div></div>
      <div class="specialty"><div class="specialty-photo" role="img" aria-label="Photograph of treatment plant equipment"></div><div class="specialty-label">Environmental</div></div>
    </div>
  </article>
</section>

</body>
</html>
```